Kelvo Brook Website

Design and implement (fully coded and ready to launch) website for a professional services company - please see the documents attached and send us an email if there are any questions
Target Market(s)
Market to potential clients about the services we offer and be able to reach us for any consulting opportunities
Industry/Entity Type
Professional Service
Coding
Coded - Design and coding required
Number of Pages Required
3 page
Requirements
Must have
- Single page website design that is SEO optimized
Blog Post
Contact US page
Cool images/ logos for the service offering - not fill the website with text/content
Must be professional looking website
Coded website should also look great on different screens - mobile, tablets etc
Nice to have
- Choose easy neutral colors that compliment the logo colors. Having said that don't use every color in the logo for the website design.
Should not have
- Too many colors and several various different fonts

```html
<!DOCTYPE html>
<html lang="en">
<head>
<meta charset="utf-8">
<title>Kelvo Brook – Data Platforms, Engineering &amp; Cloud</title>
<meta name="viewport" content="width=1200">
<link href="https://fonts.googleapis.com/css2?family=Audiowide&family=Poppins:wght@400;500;600&display=swap" rel="stylesheet">
<style>
:root{
  --red:#e8202a;
  --orange:#f26a1e;
  --magenta:#c1246b;
  --purple:#7b2f92;
  --blue:#1b5fb0;
  --ink:#151515;
  --text:#4a4a4a;
  --muted:#8a8a8a;
  --line:#dcdcdc;
  --soft:#ececec;
  --paper:#ffffff;
}
*{box-sizing:border-box;margin:0;padding:0}
html,body{width:1200px;height:3908px;overflow:hidden}
body{position:relative;background:var(--paper);font-family:"Poppins",sans-serif;color:var(--text)}
.abs{position:absolute}
.display{font-family:"Audiowide",sans-serif;color:var(--ink);font-weight:400}
p{font-size:14px;line-height:22px}
.justify{text-align:justify}
.copy p+p{margin-top:16px}

/* header */
.brand{left:88px;top:30px;display:flex;align-items:center;gap:12px}
.brand-dot{width:30px;height:30px;border-radius:50%;background:var(--red)}
.brand-name{font-family:"Audiowide",sans-serif;font-size:27px;color:var(--ink)}
.nav{left:490px;top:49px;font-size:13.5px;font-weight:500;color:var(--ink)}
.nav a{color:inherit;text-decoration:none;position:absolute;white-space:nowrap}
.nav a.active{color:var(--red)}
.social{display:flex;gap:8px}
.social span{display:block;width:25px;height:25px;border-radius:50%}
.header-social{left:1020px;top:45px}
.header-social span:nth-child(1){background:#3b5ba9}
.header-social span:nth-child(2){background:#2aa3ef}
.header-social span:nth-child(3){background:linear-gradient(135deg,#f6a03a,#d6246e,#8a39b8)}

/* hero */
.hero-bg{left:0;top:170px;width:1200px;height:420px;background:radial-gradient(ellipse 640px 220px at 180px 300px,#f1f1f4,transparent 70%),radial-gradient(ellipse 300px 260px at 1150px 260px,#f1f1f4,transparent 70%)}
.welcome{left:0;width:1200px;top:172px;text-align:center;font-size:20px;line-height:24px}
.hero-title{left:0;width:1200px;top:196px;text-align:center;font-size:72px;line-height:72px;z-index:2}
.hero-art{left:228px;top:274px;width:744px;height:176px;border-radius:18px;background:linear-gradient(90deg,#f4c9b0,#f0b7c4 35%,#d8bfe0 65%,#b9cce8)}
.hero-lead{left:340px;width:520px;top:460px;text-align:center;font-size:14.5px;line-height:22px;color:#333}
.rule{left:88px;width:1022px;top:607px;height:1px;background:var(--line)}

/* section headings */
.section-title{left:0;width:1200px;text-align:center;font-size:40px}
.underline{height:2px;width:46px;background:var(--ink)}

/* services */
.svc-icon{left:88px;top:832px;width:106px;height:108px;border-radius:14px;background:#e7e7ea}
.svc-title{left:88px;top:972px;font-size:25px}
.svc-text{left:88px;top:1016px;width:477px;color:#444}
.svc-orb{left:728px;top:758px;width:486px;height:486px;border-radius:50%;background:var(--soft)}
.svc-bubble{position:absolute;width:104px;height:104px;border-radius:50%;background:#fff;box-shadow:0 8px 24px rgba(0,0,0,.08);display:flex;align-items:center;justify-content:center}
.svc-bubble.on{background:linear-gradient(135deg,var(--red),var(--purple) 55%,var(--blue))}
.svc-label{position:absolute;left:869px;font-family:"Audiowide",sans-serif;font-size:20px;line-height:22px;color:var(--ink)}
.svc-sep{position:absolute;left:869px;width:241px;height:1px;background:#cfcfcf}

/* tech */
.tech-orb{left:-31px;top:1501px;width:456px;height:456px;border-radius:50%;background:linear-gradient(135deg,var(--red),var(--magenta) 55%,var(--purple))}
.tech-card{left:89px;top:1282px;width:396px;height:532px;background:#fff;border-radius:14px;box-shadow:0 10px 30px rgba(0,0,0,.08);padding:15px 17px;display:grid;grid-template-columns:1fr 1fr;grid-template-rows:repeat(5,1fr)}
.tech-cell{display:flex;align-items:center;justify-content:center;border-bottom:1px solid #e4e4e4}
.tech-cell:nth-child(odd){border-right:1px solid #e4e4e4}
.tech-cell:nth-last-child(-n+2){border-bottom:0}
.tech-cell i{display:block;width:44px;height:44px;border-radius:50%}
.tech-title{left:631px;top:1370px;font-size:40px;line-height:42px}
.tech-text{left:631px;top:1482px;width:479px;color:#444}
.tech-text p{font-size:13.5px}

/* team */
.team-orb{left:800px;top:1980px;width:520px;height:520px;border-radius:50%;background:var(--soft)}
.team-title{left:88px;top:2080px;font-size:40px}
.team-text{left:88px;top:2150px;width:438px;color:#444}
.team-text p{font-size:13.5px}
.member{position:absolute;width:221px;height:274px;background:#fff;border-radius:12px;box-shadow:0 8px 24px rgba(0,0,0,.08);padding:9px;text-align:center}
.member .photo{height:203px;border-radius:10px}
.member h4{font-family:"Audiowide",sans-serif;font-weight:400;font-size:16px;color:var(--ink);margin-top:12px;line-height:18px}
.member small{font-size:12px;color:var(--muted)}

/* blog */
.post{position:absolute;width:476px;height:414px;background:#fff;box-shadow:0 14px 30px rgba(0,0,0,.06)}
.post .media{height:255px;position:relative}
.tag{position:absolute;left:18px;bottom:18px;background:#fff;color:var(--ink);font-size:11px;font-weight:600;padding:3px 9px;border-radius:2px}
.more{position:absolute;right:26px;top:234px;width:42px;height:42px;border-radius:50%;background:#fff;box-shadow:0 3px 10px rgba(0,0,0,.15);display:flex;align-items:center;justify-content:center}
.more.hot{background:#f7c04a}
.post h3{font-family:"Audiowide",sans-serif;font-weight:400;font-size:22px;color:var(--ink);margin:26px 0 0 22px}
.post time{display:flex;align-items:center;gap:9px;font-size:13px;color:#555;margin:10px 0 0 22px}
.post time i{width:13px;height:12px;border:1.5px solid #bbb;border-radius:2px}
.post p{font-size:13.5px;line-height:23px;color:#555;margin:14px 22px 0 22px}

/* contact */
.contact-bg{left:0;top:3200px;width:1200px;height:708px}
.contact-title{left:605px;top:3362px;font-size:46px;line-height:50px}
.contact-sub{left:605px;top:3418px;font-size:14px;color:#444}
.field{position:absolute;left:605px;width:393px;border-bottom:1.5px solid #bdbdbd;font-size:13.5px;color:#555;padding-bottom:10px}
.send{left:877px;top:3756px;font-size:14px;font-weight:600;letter-spacing:1px;color:var(--red);border-bottom:2px solid var(--purple);padding-bottom:2px}
.foot-brand{left:180px;top:3560px;width:340px;display:flex;align-items:center;justify-content:center;gap:12px}
.foot-brand .brand-name{font-size:34px}
.foot-social{left:281px;top:3625px;gap:10px}
.foot-social span{width:38px;height:38px;background:#d6d6d6}
.foot-rule{left:88px;width:1022px;top:3839px;height:1px;background:#cfcfcf}
.copyright{left:0;width:1200px;top:3862px;text-align:center;font-size:13.5px;color:#222}
.to-top{left:1138px;top:3820px;width:36px;height:36px;border-radius:50%;background:linear-gradient(135deg,var(--red),var(--purple));display:flex;align-items:center;justify-content:center}
</style>
</head>
<body>

<header>
  <div class="abs brand"><span class="brand-dot"></span><span class="brand-name">KELVO BROOK</span></div>
  <nav class="abs nav">
    <a class="active" style="left:0">HOME</a>
    <a style="left:71px">SERVICES</a>
    <a style="left:165px">EXPERTISE</a>
    <a style="left:262px">PROFILE</a>
    <a style="left:344px">BLOG</a>
    <a style="left:411px">CONTACT US</a>
  </nav>
  <div class="abs social header-social" aria-label="Social links"><span></span><span></span><span></span></div>
</header>

<section class="hero">
  <div class="abs hero-bg"></div>
  <div class="abs display welcome">WELCOME TO</div>
  <h1 class="abs display hero-title">KELVO BROOK</h1>
  <div class="abs hero-art" role="img" aria-label="Hero illustration: colourful band with photos of professionals working on laptops"></div>
  <p class="abs hero-lead">Kelvo Brook provides end to end services in architecture, design and development of Data Platforms, Analytic workloads, Data Engineering, Cloud Engineering</p>
  <div class="abs rule"></div>
</section>

<section class="services">
  <h2 class="abs display section-title" style="top:694px">OUR SERVICES</h2>
  <div class="abs underline" style="left:577px;top:750px"></div>

  <div class="abs svc-icon" role="img" aria-label="Data engineering icon: cloud, gear and server on a monitor"></div>
  <h3 class="abs display svc-title">DATA ENGINEERING</h3>
  <p class="abs svc-text justify">Kelvo Brook employs the latest proven technologies, best practices, industry standards in building the Data Lakes that has become the business standard in any industry, or any size of Company to utilize the data it has about its customers, inventory or sales or social media posting, feedback, using the data to gain business insights on a near-real time basis to empower business leaders to make more informed decisions.</p>

  <div class="abs svc-orb"></div>
  <div class="svc-bubble" style="left:741px;top:813px">
    <svg width="56" height="48" viewBox="0 0 56 48" fill="none" stroke="#222" stroke-width="2"><rect x="20" y="2" width="16" height="10"/><path d="M28 12v8M8 20h40M8 20v8M28 20v8M48 20v8"/><rect x="2" y="28" width="12" height="10"/><rect x="22" y="28" width="12" height="10"/><rect x="42" y="28" width="12" height="10"/></svg>
  </div>
  <div class="svc-label" style="top:844px">PLATFORM<br>ARCHITECTURE</div>
  <div class="svc-sep" style="top:940px"></div>

  <div class="svc-bubble on" style="left:714px;top:951px">
    <svg width="56" height="50" viewBox="0 0 56 50" fill="none" stroke="#fff" stroke-width="2"><rect x="6" y="14" width="44" height="26" rx="2"/><path d="M22 46h12M28 40v6"/><circle cx="18" cy="27" r="5"/><rect x="28" y="20" width="16" height="6" rx="2"/><rect x="28" y="29" width="16" height="6" rx="2"/></svg>
  </div>
  <div class="svc-label" style="top:981px">DATA<br>ENGINEERING</div>
  <div class="svc-sep" style="top:1073px"></div>

  <div class="svc-bubble" style="left:741px;top:1090px">
    <svg width="60" height="52" viewBox="0 0 60 52" fill="none" stroke="#222" stroke-width="2"><path d="M16 22a10 10 0 0 1 4-18 12 12 0 0 1 22 2 9 9 0 0 1 2 16z"/><path d="M30 22v8M12 30h36M12 30v4M48 30v4"/><rect x="2" y="34" width="20" height="12"/><rect x="38" y="34" width="20" height="12"/></svg>
  </div>
  <div class="svc-label" style="top:1122px">CLOUD<br>DEVELOPMENTS</div>
</section>

<section class="expertise">
  <div class="abs tech-orb"></div>
  <div class="abs tech-card" aria-label="Technology partners">
    <div class="tech-cell"><i style="background:#f4d21f"></i></div>
    <div class="tech-cell"><i style="background:#f26a1e;border-radius:8px"></i></div>
    <div class="tech-cell"><i style="background:#2b2b2b;width:30px"></i></div>
    <div class="tech-cell"><i style="background:#d4456b"></i></div>
    <div class="tech-cell"><i style="background:#29b5e8"></i></div>
    <div class="tech-cell"><i style="background:#f79a1a;height:24px;border-radius:12px"></i></div>
    <div class="tech-cell"><i style="background:#1a73c8;border-radius:6px"></i></div>
    <div class="tech-cell"><i style="background:#2e8fd8"></i></div>
    <div class="tech-cell"><i style="background:#3aa3e8;height:28px;border-radius:4px"></i></div>
    <div class="tech-cell"><i style="background:#f36d1f"></i></div>
  </div>
  <h2 class="abs display tech-title">OUR TECHNOLOGY<br>EXPERTISE</h2>
  <div class="abs underline" style="left:631px;top:1465px"></div>
  <div class="abs tech-text copy">
    <p class="justify">Kelvo Brook is a company which intends to be in front of the client's needs, deeply understanding clients' business and delivering and optimizing solutions from the initial phase of scoping the requirements, up to the final delivery, maintenance and continuous upgrade. Kelvo Brook focuses always from the customer perspective to grasp their business need for the IT solutions they deliver.</p>
    <p class="justify">Our team operates with enthusiasm and flexibility. We are focused on our customers, being their reliable partner for services and solutions, working together on a partnership basis, helping clients with challenging problems to solve.</p>
  </div>
</section>

<section class="team">
  <div class="abs team-orb"></div>
  <h2 class="abs display team-title">MEET THE TEAM</h2>
  <div class="abs team-text copy">
    <p class="justify">Arun manages all the client interactions and engineering team at Kelvo Brook. Arun has over 15 years of experience in the technology before he founded Kelvo Brook. He managed development of large scale enterprise wide, performance, scalable, real time software solutions in Tele communications, Gaming, Finance, and Insurance Industries.</p>
    <p class="justify">He spends time working on open source projects, contributions to Kestrel Store, Flux connectors and Flux JobRunner &amp; other projects. In free time, Arun enjoys travelling to historical places, playing sports run, bike, tennis, ping-pong &amp; spending time with family.</p>
  </div>

  <div class="member" style="left:649px;top:1952px"><div class="photo" role="img" aria-label="Team member photo: woman working at a laptop" style="background:linear-gradient(135deg,#e3ddd5,#c9b37a)"></div><h4>ARUN VELIS</h4><small>Founder</small></div>
  <div class="member" style="left:649px;top:2245px"><div class="photo" role="img" aria-label="Team member photo: woman with laptop on a sofa" style="background:linear-gradient(135deg,#d8d8d8,#a9c4d6)"></div><h4>ARUN VELIS</h4><small>Founder</small></div>
  <div class="member" style="left:888px;top:2100px"><div class="photo" role="img" aria-label="Team member photo: man typing on a laptop" style="background:linear-gradient(135deg,#cfd6dc,#2d5a8a)"></div><h4>ARUN VELIS</h4><small>Founder</small></div>
</section>

<section class="blog">
  <h2 class="abs display section-title" style="top:2623px">LATEST FROM OUR BLOG</h2>
  <div class="abs underline" style="left:577px;top:2679px"></div>

  <article class="post" style="left:97px;top:2711px">
    <div class="media" role="img" aria-label="Photo of a smiling team standing in an office" style="background:linear-gradient(160deg,#c9cdd2,#6b7079)"><span class="tag">NEWS</span></div>
    <span class="more"><svg width="10" height="14" viewBox="0 0 10 14" fill="none" stroke="#333" stroke-width="1.6"><path d="M2 1l6 6-6 6"/></svg></span>
    <h3>BLOG HEADING HERE</h3>
    <time><i></i>25-08-2018</time>
    <p>Aenean sollicitudin lorem quis bibendum auctor nisi elit Duis sed odio sit amet nibh vulputate cursus a sit amet...</p>
  </article>

  <article class="post" style="left:625px;top:2711px">
    <div class="media" role="img" aria-label="Photo of a smiling man working at a laptop" style="background:linear-gradient(160deg,#9aa0a6,#3d4248)"><span class="tag">EVENT</span></div>
    <span class="more hot"><svg width="10" height="14" viewBox="0 0 10 14" fill="none" stroke="#333" stroke-width="1.6"><path d="M2 1l6 6-6 6"/></svg></span>
    <h3>BLOG HEADING HERE</h3>
    <time><i></i>25-08-2018</time>
    <p>Aenean sollicitudin lorem quis bibendum auctor nisi elit Duis sed odio sit amet nibh vulputate cursus a sit amet...</p>
  </article>
</section>

<section class="contact">
  <svg class="abs contact-bg" viewBox="0 3200 1200 708" width="1200" height="708" preserveAspectRatio="none" aria-hidden="true">
    <defs><linearGradient id="swoosh" x1="0" x2="1"><stop offset="0" stop-color="#e8202a"/><stop offset=".5" stop-color="#7b2f92"/><stop offset="1" stop-color="#1b5fb0"/></linearGradient></defs>
    <path d="M0 3438 C300 3250 700 3190 1200 3345 L1200 3908 L0 3908 Z" fill="#ececec"/>
    <path d="M0 3438 C300 3250 700 3190 1200 3345 L1200 3372 C700 3220 320 3268 0 3438 Z" fill="url(#swoosh)"/>
  </svg>
  <h2 class="abs display contact-title">CONTACT</h2>
  <div class="abs contact-sub">Contact us &amp; find how can benefit your company.</div>
  <div class="field" style="top:3468px">Enter your name...</div>
  <div class="field" style="top:3518px">Enter your Email..</div>
  <div class="field" style="top:3568px">Enter your Phone Number...</div>
  <div class="field" style="top:3621px;height:100px">Enter your Message...</div>
  <div class="abs send">SEND MESSAGE</div>

  <div class="abs foot-brand"><span class="brand-dot"></span><span class="brand-name">KELVO BROOK</span></div>
  <div class="abs social foot-social" aria-label="Social links"><span></span><span></span><span></span></div>

  <div class="abs foot-rule"></div>
  <div class="abs copyright">© Copyright 2020 All Rights Reserved</div>
  <div class="abs to-top"><svg width="12" height="8" viewBox="0 0 12 8" fill="none" stroke="#fff" stroke-width="1.8"><path d="M1 7l5-5 5 5"/></svg></div>
</section>

</body>
</html>
```